Organic Coconut oil

A label for a 500ml jar of organic coconut oil
The product is raw cold pressed virgin coconut oil
Target Market(s)
All health conscious individuals
Industry/Entity Type
Product
Requirements
Must have
- Virgin
Raw
Cold pressed
Organic
Product name tovi coconut oil

```html
<!DOCTYPE html>
<html lang="en">
<head>
<meta charset="utf-8">
<title>Tovi Coconut Oil – Jar Label</title>
<link rel="stylesheet" href="https://fonts.googleapis.com/css2?family=Gentium+Book+Plus:wght@400&display=swap">
<style>
  :root {
    --canvas-bg: #ffffff;
    --label-bg: #e8ecc0;
    --ink: #111111;
    --shell-brown: #6e5437;
    --leaf-green: #6aa232;
    --flesh-white: #f4f4f2;
  }
  * { margin: 0; padding: 0; box-sizing: border-box; }
  html, body {
    width: 1200px;
    height: 1000px;
    overflow: hidden;
    background: var(--canvas-bg);
  }
  .canvas {
    position: relative;
    width: 1200px;
    height: 1000px;
  }
  .label {
    position: absolute;
    left: 245px;
    top: 253px;
    width: 710px;
    height: 494px;
    background: var(--label-bg);
    font-family: "Gentium Book Plus", Georgia, serif;
    color: var(--ink);
  }
  .label__illustration {
    position: absolute;
    left: 18px;
    top: 110px;
    width: 372px;
    height: 365px;
  }
  .label__brand {
    position: absolute;
    left: 405px;
    top: 48px;
    font-size: 120px;
    line-height: 1;
    font-weight: 400;
  }
  .label__product {
    position: absolute;
    left: 427px;
    top: 170px;
    font-size: 34px;
    line-height: 1;
    font-weight: 400;
  }
  .label__claims {
    position: absolute;
    left: 430px;
    top: 282px;
    font-size: 26px;
    line-height: 40px;
    list-style: none;
  }
  .label__volume {
    position: absolute;
    left: 555px;
    top: 432px;
    font-size: 32px;
    line-height: 1;
  }
</style>
</head>
<body>
<main class="canvas">
  <section class="label">
    <svg class="label__illustration" viewBox="0 0 372 365" role="img" aria-label="Illustration of a halved coconut on a green leaf with coconut oil pouring out">
      <defs>
        <radialGradient id="coconut-tones" cx="0.5" cy="0.45" r="0.6">
          <stop offset="0" stop-color="var(--flesh-white)"/>
          <stop offset="0.55" stop-color="var(--shell-brown)" stop-opacity="0.75"/>
          <stop offset="1" stop-color="var(--leaf-green)" stop-opacity="0.7"/>
        </radialGradient>
      </defs>
      <ellipse cx="186" cy="182" rx="184" ry="180" fill="url(#coconut-tones)"/>
    </svg>
    <h1 class="label__brand">Tovi</h1>
    <p class="label__product">Coconut Oil</p>
    <ul class="label__claims">
      <li>Raw, Organic</li>
      <li>Cold Pressed</li>
      <li>Virgin Coconut Oil</li>
    </ul>
    <p class="label__volume">500ml</p>
  </section>
</main>
</body>
</html>
```